Oakridge Abode & Nest Upkeep - Maintenance & Improvements

Handyman service - Total home improvement and maintenance

We do everything indoors, ie. carpentry, and outdoors, ie. garden maintenance

No job too small or too unusual

7 Days per week
Updates

I want the overall impression not to favour either gender ... eg. maybe don't use the word Handy'man' because we also have a Tinkerella service .... but just stay with a generic theme of home improvement and maintenance

Industry/Entity Type

Home Improvement

Contact Information for Business Card

Oakridge Abode & Nest Upkeep
7 Days per Week
Total Home Maintenance and Improvements
Handyman | Tinkerella | The (Solo) Spark Kit
Ph: 0491 573 862
www.oakridgeabodenest.com.au

Requirements
Must have
• The black and white image of various workers, as per attached

```html
<!DOCTYPE html>
<html lang="en">
<head>
<meta charset="utf-8">
<title>Oakridge Abode &amp; Nest Upkeep – Business Card</title>
<link href="https://fonts.googleapis.com/css2?family=Open+Sans:wght@400;600;700&display=swap" rel="stylesheet">
<style>
  :root {
    --page-bg: #e9e6e2;
    --card-orange: #db5a2c;
    --card-orange-deep: #c94a20;
    --ink: #1c1410;
    --photo-sky: #7fb3c8;
    --photo-green: #3f6a2e;
    --photo-wood: #b8742f;
    --photo-stone: #d9d4cc;
  }
  * { box-sizing: border-box; margin: 0; padding: 0; }
  html, body {
    width: 1200px; height: 900px; overflow: hidden;
    background: var(--page-bg);
    font-family: "Open Sans", Arial, sans-serif;
    color: var(--ink);
  }
  .stage {
    width: 1200px; height: 900px;
    display: flex; align-items: center; justify-content: center;
  }
  .business-card {
    position: relative;
    width: 1050px; height: 600px;
    background: linear-gradient(160deg, var(--card-orange) 0%, var(--card-orange-deep) 100%);
    box-shadow: 0 12px 30px rgba(0,0,0,0.25);
    overflow: hidden;
  }
  .card-photo {
    position: absolute; left: 0; top: 0;
    width: 400px; height: 600px;
    background: linear-gradient(200deg, var(--photo-green) 0%, var(--photo-wood) 38%, var(--photo-sky) 62%, var(--photo-stone) 100%);
  }
  .brand-block {
    position: absolute; right: 50px; top: 48px;
    text-align: right;
  }
  .brand-lead {
    font-weight: 700; font-size: 30px; line-height: 1.1;
  }
  .brand-name {
    font-weight: 400; font-size: 56px; line-height: 1.1;
    letter-spacing: 0.5px;
  }
  .brand-tagline {
    font-size: 24px; line-height: 1.25; margin-top: 6px;
  }
  .contact-block {
    position: absolute; right: 50px; top: 300px;
    text-align: right;
  }
  .service-name { font-weight: 700; font-size: 34px; line-height: 1.2; }
  .service-line {
    font-size: 28px; line-height: 1.3;
    display: flex; align-items: center; justify-content: flex-end; gap: 10px;
  }
  .service-line svg { width: 26px; height: 26px; flex: none; }
  .contact-line { margin-top: 10px; }
  .web-address {
    position: absolute; right: 50px; bottom: 48px;
    font-size: 32px; letter-spacing: 0.5px;
  }
</style>
</head>
<body>
<main class="stage">
  <article class="business-card">
    <div class="card-photo" role="img" aria-label="Photo of a garden patio with a timber pergola, outdoor wicker lounge with orange cushions and a blue pool"></div>

    <header class="brand-block">
      <div class="brand-lead">Oakridge</div>
      <h1 class="brand-name">Abode &amp; Nest Upkeep</h1>
      <p class="brand-tagline">7 Days per Week Total Home Maintenance<br>Improvements Handyman</p>
    </header>

    <section class="contact-block">
      <div class="service-name">Tinkerella</div>
      <div class="service-line">The (Solo) Spark Kit
        <svg viewBox="0 0 24 24" aria-hidden="true"><path fill="currentColor" d="M6.6 10.8c1.4 2.8 3.8 5.1 6.6 6.6l2.2-2.2c.3-.3.7-.4 1-.2 1.1.4 2.3.6 3.6.6.6 0 1 .4 1 1V20c0 .6-.4 1-1 1C10.6 21 3 13.4 3 4c0-.6.4-1 1-1h3.5c.6 0 1 .4 1 1 0 1.3.2 2.5.6 3.6.1.3 0 .7-.2 1z"/></svg>
      </div>
      <div class="service-line contact-line">0491 573 862
        <svg viewBox="0 0 24 24" aria-hidden="true"><g fill="none" stroke="currentColor" stroke-width="1.8"><circle cx="12" cy="12" r="9.5"/><ellipse cx="12" cy="12" rx="4" ry="9.5"/><path d="M2.5 12h19M4 7h16M4 17h16"/></g></svg>
      </div>
    </section>

    <p class="web-address">www.oakridgeabodenest.com.au</p>
  </article>
</main>
</body>
</html>
```